Waste management company seeks a new website design

We need a website design for an environmental services company called 'Vilumetsa Kogumisteenused.' We manage waste collection and recycling for 100K+ households and businesses across Estonia. Please use logos and colors from attached CVI file. The design should be extensively usable for our self-service portal and have a mobile-first approach as it will be turned into an app in the future. The new website should highlight our commitment to sustainability and provide easy access to our services with a clean, modern design. UX inspiration from https://trevix.eu/et-ee/

```html
<!DOCTYPE html>
<html lang="et">
<head>
<meta charset="utf-8">
<title>Vilumetsa Kogumisteenused</title>
<link href="https://fonts.googleapis.com/css2?family=Oswald:wght@500;600;700&family=Poppins:wght@400;500;600&display=swap" rel="stylesheet">
<style>
:root{
  --lime:#d6de2c;
  --lime-bright:#e3ec2d;
  --lime-pale:#f3f7d2;
  --ink:#1c1c1c;
  --body:#3a3a3a;
  --muted:#8a8a8a;
  --brand-grey:#7d716c;
  --soft-bg:#f6f6f6;
  --field:#f8f8f8;
  --footer:#0d0d0d;
  --white:#ffffff;
}
*{margin:0;padding:0;box-sizing:border-box}
html,body{width:1200px;height:4769px;overflow:hidden}
body{position:relative;background:var(--white);font-family:'Poppins',sans-serif;color:var(--body)}
.abs{position:absolute}
h1,h2,h3,.btn,.tag{font-family:'Oswald',sans-serif;text-transform:uppercase;color:var(--ink)}
.btn{position:absolute;display:flex;align-items:center;justify-content:center;background:var(--lime);border-radius:6px;font-weight:600;font-size:15px;letter-spacing:.3px}
p.copy{font-size:14.5px;line-height:30px;color:var(--body)}

.site-header{position:absolute;left:0;top:0;width:1200px;height:109px;background:var(--white);z-index:3}
.site-header .topline{position:absolute;left:0;top:0;width:1200px;height:4px;background:linear-gradient(90deg,#fff 0%,#fff 40%,var(--lime) 100%)}
.brand{position:absolute;display:flex;align-items:center;gap:12px}
.brand .mark{border-radius:50%;background:var(--lime)}
.brand .name{font-family:'Poppins',sans-serif;font-weight:500;color:var(--brand-grey)}
.contact-chip{position:absolute;display:flex;align-items:center;gap:14px}
.chip-icon{width:42px;height:42px;border-radius:50%;display:flex;align-items:center;justify-content:center}
.login{left:983px;top:26px;width:95px;height:37px;border-radius:20px;font-size:13px}
.main-nav{position:absolute;left:430px;top:100px;width:560px;height:40px;z-index:4}
.main-nav ul{position:absolute;inset:0;list-style:none;font-size:12.5px;color:var(--ink)}
.main-nav li{position:absolute;top:9px}

.hero{position:absolute;left:0;top:109px;width:1200px;height:587px;background:linear-gradient(180deg,#2f2a26 0%,#4a3f37 45%,#3a332e 75%,#5a4e45 100%)}
.hero .tag{position:absolute;left:111px;top:169px;height:27px;padding:0 16px;background:var(--lime);font-size:16px;font-weight:500;display:flex;align-items:center}
.hero h1{position:absolute;left:109px;top:200px;font-size:78px;line-height:82px;color:var(--white);font-weight:700;letter-spacing:1px}

.about-frame{position:absolute;left:87px;top:782px;width:386px;height:520px;border:1.5px solid #e4e89a;border-radius:14px}
.media{position:absolute;border-radius:14px}
.section-title{position:absolute;font-size:36px;font-weight:600;letter-spacing:.3px}

.services{position:absolute;left:0;top:1467px;width:1200px;height:650px;background:var(--soft-bg)}
.service{position:absolute;width:260px;text-align:center}
.service h3{font-size:19px;font-weight:500;margin-top:0}
.service p{font-size:12.5px;line-height:26px;color:var(--body);margin-top:16px}
.service .more{display:inline-block;margin-top:10px;font-family:'Oswald',sans-serif;font-size:12.5px;color:var(--lime);text-decoration:underline;text-transform:uppercase}

.team-panel{position:absolute;left:98px;top:2937px;width:989px;height:308px;background:var(--lime-bright);border-radius:16px}
.member-card{position:absolute;width:290px;background:var(--white);box-shadow:0 6px 22px rgba(0,0,0,.1);padding:22px 20px}
.member-card h3{font-size:17px;font-weight:500}
.member-card .role{font-size:11px;color:var(--muted);margin-top:2px}
.member-card .rule{width:40px;height:2px;background:var(--lime);margin-top:6px}
.member-card .stars{color:#f0a81a;font-size:14px;letter-spacing:2px;margin-top:4px}
.member-card p{font-size:11.5px;line-height:21px;color:var(--ink);margin-top:10px}

.field{position:absolute;background:var(--white);box-shadow:0 3px 12px rgba(0,0,0,.09);border-radius:4px;font-size:13px;color:#9a9a9a;padding:12px 16px}

.site-footer{position:absolute;left:0;top:4213px;width:1200px;height:556px;background:var(--footer);color:var(--white)}
.site-footer h3{position:absolute;color:var(--white);font-size:18px;font-weight:500}
.site-footer .small{position:absolute;font-size:13.5px;line-height:24px;color:var(--white)}
.foot-nav{position:absolute;top:201px;font-size:12.5px;color:var(--white)}
.social{position:absolute;top:386px;width:14px;height:14px;border-radius:50%;background:var(--white)}
</style>
</head>
<body>

<header class="site-header">
  <div class="topline"></div>
  <div class="brand" style="left:111px;top:28px">
    <div class="mark" style="width:50px;height:50px"></div>
    <div class="name" style="font-size:21px;line-height:24px">Vilumetsa<br>Kogumisteenused</div>
  </div>
  <div class="contact-chip" style="left:444px;top:22px">
    <div class="chip-icon" style="background:var(--brand-grey)">
      <svg width="18" height="18" viewBox="0 0 24 24"><path d="M6.6 10.8a15 15 0 006.6 6.6l2.2-2.2c.3-.3.7-.4 1-.2 1.1.4 2.3.6 3.6.6.6 0 1 .4 1 1V20c0 .6-.4 1-1 1A17 17 0 013 4c0-.6.4-1 1-1h3.5c.6 0 1 .4 1 1 0 1.3.2 2.5.6 3.6.1.3 0 .7-.2 1z" fill="#1c1c1c"/></svg>
    </div>
    <div>
      <div style="font-family:'Oswald',sans-serif;font-size:14px;font-weight:500;color:var(--ink)">CALL US</div>
      <div style="font-size:20px;font-weight:500;color:var(--brand-grey);line-height:24px">+372 5550 1420</div>
    </div>
  </div>
  <div class="contact-chip" style="left:694px;top:25px">
    <div class="chip-icon" style="background:var(--lime)">
      <svg width="16" height="20" viewBox="0 0 16 20"><path d="M8 0a7 7 0 00-7 7c0 5 7 13 7 13s7-8 7-13a7 7 0 00-7-7zm0 9.5A2.5 2.5 0 118 4.5a2.5 2.5 0 010 5z" fill="#1c1c1c"/></svg>
    </div>
    <div style="font-size:13px;line-height:24px;color:var(--ink)">112 bVilumetsa Kogumisteenused<br>dolor sit amet, consectetur</div>
  </div>
  <div class="btn login">LOGIN</div>
</header>

<nav class="main-nav">
  <svg class="abs" style="left:0;top:0" width="560" height="40"><path d="M0 0H560L546 32Q542 40 532 40H28Q18 40 14 32Z" fill="#fff"/></svg>
  <ul>
    <li style="left:40px">Home</li>
    <li style="left:121px">About Us</li>
    <li style="left:219px">Our Services</li>
    <li style="left:340px">Testimonials</li>
    <li style="left:458px">Contact us</li>
  </ul>
</nav>

<section class="hero" role="img" aria-label="Photo of a straight road running through a dark pine forest">
  <div class="tag">WELCOME TO</div>
  <h1>Vilumetsa<br>Kogumisteenused</h1>
  <div class="abs" style="left:0;top:414px;width:124px;height:2px;background:var(--white)"></div>
  <svg class="abs" style="left:122px;top:389px" width="52" height="52"><circle cx="26" cy="26" r="24" fill="none" stroke="#fff" stroke-width="2"/><circle cx="26" cy="26" r="18" fill="var(--lime)"/><path d="M22 19L33 26L22 33Z" fill="#1c1c1c"/></svg>
</section>

<section class="about">
  <svg class="abs" style="left:66px;top:826px" width="64" height="64"><circle cx="32" cy="30" r="27" fill="none" stroke="#2b5a9c" stroke-width="1.5"/></svg>
  <svg class="abs" style="left:1080px;top:780px" width="60" height="60"><path d="M8 40A26 26 0 1 1 52 40" fill="none" stroke="#1c1c1c" stroke-width="1.5"/></svg>
  <div class="about-frame"></div>
  <div class="media" style="left:113px;top:809px;width:385px;height:532px;background:linear-gradient(160deg,#c98a52 0%,#a4683f 40%,#6e3b2e 75%,#4a2a28 100%)" role="img" aria-label="Portrait photo of a young woman in a knit hat breathing fresh air outdoors"></div>
  <h2 class="section-title" style="left:550px;top:832px">About Vilumetsa Kogumisteenused</h2>
  <div class="abs" style="left:554px;top:900px;width:535px">
    <p class="copy">Lorem ipsum dolor sit amet, consectetur adipiscing elit, sed do eiusmod tempor incididunt ut labore et dolore magna aliqua. Quis ipsum sus-pendisse ultrices gravida. Risus commodo viverra maecenas accumsan lacus vel facilisis.</p>
    <p class="copy" style="margin-top:30px">Lorem ipsum dolor sit amet, consectetur adipiscing elit, sed do eiusmod tempor incididunt ut labore et dolore magna aliqua. Quis ipsum sus-pendisse ultrices gravida. Risus commodo viverra maecenas accumsan lacus vel facilisis.</p>
    <p class="copy" style="margin-top:30px">Lorem ipsum dolor sit amet, consectetur adipiscing elit, sed do eiusmod tempor incididunt ut labore et dolore magna aliqua.</p>
  </div>
  <div class="btn" style="left:552px;top:1278px;width:160px;height:53px">LEARN MORE</div>
</section>

<section class="services">
  <h2 class="section-title" style="left:0;width:1200px;text-align:center;top:56px">Our Services</h2>
  <div class="abs" style="left:300px;top:219px;width:610px;height:2px;background:#ececec"></div>

  <svg class="abs" style="left:232px;top:152px" width="122" height="138"><polygon points="61,0 122,34 122,104 61,138 0,104 0,34" fill="var(--lime)"/>
    <g fill="none" stroke="#1c1c1c" stroke-width="2.2" stroke-linecap="round"><circle cx="66" cy="60" r="10"/><circle cx="66" cy="60" r="4"/><path d="M36 78h14l10 6h14l10-6"/><path d="M36 88h18l14 6 20-12"/></g></svg>
  <svg class="abs" style="left:537px;top:156px" width="122" height="138"><polygon points="61,0 122,34 122,104 61,138 0,104 0,34" fill="var(--lime)"/>
    <g fill="none" stroke="#1c1c1c" stroke-width="2.2" stroke-linecap="round"><circle cx="44" cy="52" r="5"/><circle cx="61" cy="46" r="5"/><circle cx="78" cy="52" r="5"/><path d="M34 72v-6a8 8 0 0116 0M51 64v-4a10 10 0 0120 0v4M72 66a8 8 0 0116 0v6"/><circle cx="61" cy="88" r="9"/><circle cx="61" cy="88" r="3"/></g></svg>
  <svg class="abs" style="left:848px;top:152px" width="122" height="138"><polygon points="61,0 122,34 122,104 61,138 0,104 0,34" fill="var(--lime)"/>
    <g fill="none" stroke="#1c1c1c" stroke-width="2.2" stroke-linecap="round"><rect x="45" y="53" width="32" height="32" rx="3"/><rect x="54" y="66" width="14" height="11"/><path d="M56 66v-4a5 5 0 0110 0v4M52 53v-10M61 53v-12M70 53v-10M52 85v10M61 85v12M70 85v10M45 62H34M45 76H34M77 62h11M77 76h11"/></g></svg>

  <div class="service" style="left:163px;top:323px"><h3>Lorem Ipsum</h3><p>Lorem ipsum dolor sit amet, consectetur adipiscing elit, sed do eiusmod tempor incididunt ut labore et dolore magna aliqua. Quis ipsum suspendisse</p><span class="more">Learn More</span></div>
  <div class="service" style="left:468px;top:327px"><h3>Lorem Ipsum</h3><p>Lorem ipsum dolor sit amet, consectetur adipiscing elit, sed do eiusmod tempor incididunt ut labore et dolore magna aliqua. Quis ipsum suspendisse</p><span class="more">Learn More</span></div>
  <div class="service" style="left:779px;top:323px"><h3>Lorem Ipsum</h3><p>Lorem ipsum dolor sit amet, consectetur adipiscing elit, sed do eiusmod tempor incididunt ut labore et dolore magna aliqua. Quis ipsum suspendisse</p><span class="more">Learn More</span></div>

  <div class="btn" style="left:531px;top:541px;width:113px;height:41px;font-size:13px">VIEW MORE</div>
</section>

<section class="what-we-do">
  <div class="abs" style="left:936px;top:2199px;width:194px;height:194px;border-radius:50%;background:var(--lime)"></div>
  <div class="abs" style="left:574px;top:2473px;width:444px;height:444px;border-radius:50%;background:var(--lime-pale)"></div>
  <h2 class="section-title" style="left:91px;top:2270px">What We Do</h2>
  <div class="abs" style="left:93px;top:2339px;width:540px">
    <p class="copy">Lorem ipsum dolor sit amet, consectetur adipiscing elit, sed do eiusmod tempor incididunt ut labore et dolore magna aliqua. Quis ipsum sus-pendisse ultrices gravida. Risus commodo viverra maecenas accumsan lacus vel facilisis.</p>
    <p class="copy" style="margin-top:30px">Lorem ipsum dolor sit amet, consectetur adipiscing elit, sed do eiusmod tempor incididunt ut labore et dolore magna aliqua. Quis ipsum sus-pendisse ultrices gravida. Risus commodo viverra maecenas accumsan lacus vel facilisis.</p>
    <p class="copy" style="margin-top:30px">Lorem ipsum dolor sit amet, consectetur adipiscing elit, sed do eiusmod tempor incididunt ut labore et dolore magna aliqua. Quis ipsum sus-</p>
  </div>
  <div class="btn" style="left:93px;top:2728px;width:161px;height:54px">LEARN MORE</div>
  <div class="media" style="left:678px;top:2270px;width:386px;height:530px;background:linear-gradient(170deg,#b7a98a 0%,#6d7356 30%,#2f4a33 60%,#8d8a80 100%)" role="img" aria-label="Photo of a row of green recycling bins on a city pavement"></div>
</section>

<section class="team">
  <div class="team-panel"></div>
  <h2 class="section-title" style="left:98px;width:989px;text-align:center;top:3000px;font-size:38px">Our Team</h2>
  <svg class="abs" style="left:79px;top:3215px" width="10" height="14"><path d="M7 2L2 7L7 12" fill="none" stroke="#555" stroke-width="1.5"/></svg>

  <div class="abs" style="left:135px;top:3106px;width:277px;height:279px;background:linear-gradient(180deg,#d9d9d9,#b8b4b0)" role="img" aria-label="Portrait photo of team member Marten Kask"></div>
  <div class="member-card" style="left:302px;top:3293px">
    <h3>Marten Kask</h3><div class="role">Lorem ipsum</div><div class="rule"></div>
    <div class="stars">★★★☆☆</div>
    <p>Lorem ipsum dolor sit amet, consectetur adipiscing elit, sed do eiusmod tempor inci-didunt ut labore et dolore magna aliqua. Quis ipsum suspendisse ultrices gravida.</p>
  </div>

  <div class="abs" style="left:635px;top:3106px;width:278px;height:279px;background:linear-gradient(180deg,#dcdcdc,#a88a6e)" role="img" aria-label="Portrait photo of team member Liisa Tamm"></div>
  <div class="member-card" style="left:802px;top:3293px">
    <h3>Liisa Tamm</h3><div class="role">Lorem ipsum</div><div class="rule"></div>
    <div class="stars">★★★☆☆</div>
    <p>Lorem ipsum dolor sit amet, consectetur adipiscing elit, sed do eiusmod tempor inci-didunt ut labore et dolore magna</p>
  </div>
</section>

<section class="contact">
  <div class="abs" style="left:159px;top:3608px;width:317px;height:498px;background:linear-gradient(180deg,#e4e6ec 0%,#cfd2d6 30%,#4f5a55 55%,#8a7a5e 80%,#a08d6c 100%)" role="img" aria-label="Photo of a misty pine forest edge above a dry meadow"></div>
  <h2 class="section-title" style="left:511px;top:3668px">Get In Touch</h2>
  <div class="abs" style="left:515px;top:3737px;font-size:20px;color:var(--ink)">Lorem ipsum dolor sit amet, consectetur</div>
  <div class="field" style="left:511px;top:3789px;width:246px;height:39px">First Name</div>
  <div class="field" style="left:781px;top:3789px;width:247px;height:39px">Last Name</div>
  <div class="field" style="left:511px;top:3852px;width:246px;height:39px">Phone</div>
  <div class="field" style="left:781px;top:3852px;width:247px;height:39px">Email</div>
  <div class="field" style="left:511px;top:3914px;width:517px;height:40px">Message</div>
  <div class="btn" style="left:515px;top:3980px;width:128px;height:48px;font-family:'Poppins',sans-serif;font-size:14px">SUBMIT</div>
</section>

<footer class="site-footer">
  <div class="brand" style="left:350px;top:68px">
    <div class="mark" style="width:90px;height:90px"></div>
    <div class="name" style="font-size:38px;line-height:44px">Vilumetsa<br>Kogumisteenused</div>
  </div>
  <div class="foot-nav" style="left:356px">Home</div>
  <div class="foot-nav" style="left:438px">About Us</div>
  <div class="foot-nav" style="left:537px">Our Services</div>
  <div class="foot-nav" style="left:657px">Testimonials</div>
  <div class="foot-nav" style="left:776px">Contact us</div>

  <h3 style="left:117px;top:264px">About Us</h3>
  <div class="small" style="left:114px;top:302px;width:230px">Lorem ipsum dolor sit amet, consectetur adipiscing elit, sed do eiusmod tempor incididunt</div>

  <h3 style="left:444px;top:264px">Subscribe To Our Newsletter</h3>
  <div class="abs" style="left:417px;top:306px;width:329px;height:50px;border:1.5px solid var(--white);display:flex;align-items:center;padding:0 10px 0 18px;justify-content:space-between">
    <span style="font-size:14px">Enter Your Email</span>
    <span class="btn" style="position:static;width:112px;height:32px;font-family:'Poppins',sans-serif;font-size:11.5px;border-radius:3px">SUBSCRIBE</span>
  </div>
  <div class="social" style="left:533px"></div>
  <div class="social" style="left:561px"></div>
  <div class="social" style="left:590px"></div>
  <div class="social" style="left:619px"></div>

  <h3 style="left:820px;top:264px">Contact Us</h3>
  <svg class="abs" style="left:820px;top:307px" width="11" height="14" viewBox="0 0 16 20"><path d="M8 0a7 7 0 00-7 7c0 5 7 13 7 13s7-8 7-13a7 7 0 00-7-7zm0 9.5A2.5 2.5 0 118 4.5a2.5 2.5 0 010 5z" fill="#fff"/></svg>
  <div class="small" style="left:842px;top:300px">112 bVilumetsa Kogumisteenused<br>dolor sit amet, consectetur</div>
  <svg class="abs" style="left:820px;top:357px" width="13" height="13" viewBox="0 0 24 24"><path d="M6.6 10.8a15 15 0 006.6 6.6l2.2-2.2c.3-.3.7-.4 1-.2 1.1.4 2.3.6 3.6.6.6 0 1 .4 1 1V20c0 .6-.4 1-1 1A17 17 0 013 4c0-.6.4-1 1-1h3.5c.6 0 1 .4 1 1 0 1.3.2 2.5.6 3.6.1.3 0 .7-.2 1z" fill="#fff"/></svg>
  <div class="small" style="left:844px;top:351px">372-555-0142</div>
  <svg class="abs" style="left:820px;top:384px" width="14" height="11"><rect x="1" y="1" width="12" height="9" fill="none" stroke="#fff" stroke-width="1.3"/><path d="M1 1l6 5 6-5" fill="none" stroke="#fff" stroke-width="1.3"/></svg>
  <div class="small" style="left:844px;top:377px">info@vilumetsakogumine.ee</div>

  <div class="small" style="left:0;width:1200px;text-align:center;top:490px;font-size:13.5px">© Copyrights 2024 Vilumetsa Kogumisteenused &nbsp;|&nbsp; All Rights Reserved</div>
</footer>

</body>
</html>
```